" Somos um provedor de internet que fornece principalmente o serviço de internet por fibra óptica. Também temos TV por assinatura via satélite e telefonia IP "

```html
<!DOCTYPE html>
<html lang="pt-BR">
<head>
<meta charset="utf-8">
<title>Fibravia — Internet fibra óptica</title>
<link rel="stylesheet" href="https://fonts.googleapis.com/css2?family=Open+Sans:ital,wght@0,400;0,600;0,700;0,800;1,400;1,600&display=swap">
<style>
:root{
  --blue:#2a8fd0;
  --blue-dark:#1f6fa8;
  --navy:#1d3a5c;
  --text:#555c66;
  --muted:#9aa1a8;
  --line:#e6e8eb;
  --band:#f1f2f4;
  --white:#ffffff;
  --hero-top:#3d86cf;
  --hero-bottom:#5f9fdc;
}
*{margin:0;padding:0;box-sizing:border-box}
html,body{width:1200px;height:1200px;overflow:hidden;background:var(--white);font-family:"Open Sans",Arial,sans-serif;color:var(--text)}
.page{position:relative;width:1200px;height:1200px}

.topbar{position:absolute;left:300px;top:0;width:740px;height:24px;display:flex;align-items:center;justify-content:space-between;font-size:8px;color:var(--muted);border-bottom:1px solid var(--line)}
.topbar .social{display:flex;gap:10px}
.topbar .social span{width:9px;height:9px;border-radius:50%;background:#c4c9ce;display:block}

.header{position:absolute;left:300px;top:26px;width:740px;height:48px;display:flex;align-items:center;justify-content:space-between}
.brand{display:flex;align-items:center;gap:8px;font-weight:800;font-size:17px;color:var(--navy);letter-spacing:.5px}
.brand .mark{width:26px;height:26px;background:var(--navy)}
.nav{display:flex;gap:22px;font-size:8.5px;color:var(--text);text-transform:uppercase;font-weight:600}

.hero{position:absolute;left:154px;top:77px;width:892px;height:303px;background:linear-gradient(180deg,var(--hero-top) 0%,var(--hero-bottom) 100%);overflow:hidden}
.hero-copy{position:absolute;left:237px;top:100px;width:340px;color:var(--white)}
.hero-copy h1{font-size:31px;font-weight:800;line-height:1.05}
.hero-copy h2{font-size:19px;font-weight:600;font-style:italic;margin-top:2px}
.hero-copy p{font-size:8.5px;line-height:1.5;margin-top:12px;width:320px}
.hero-actions{display:flex;gap:12px;margin-top:14px}
.btn{display:inline-block;padding:6px 16px;font-size:7.5px;font-weight:700;text-transform:uppercase}
.btn-primary{background:var(--blue-dark);color:var(--white)}
.btn-light{background:var(--white);color:var(--navy)}
.hero-note{position:absolute;left:237px;bottom:12px;font-size:7.5px;color:var(--white)}
.hero-note b{font-weight:700}

.segments{position:absolute;left:340px;top:425px;width:520px;display:flex;justify-content:space-between}
.segment{width:120px;text-align:center}
.segment .icon{width:38px;height:38px;margin:0 auto;display:flex;align-items:center;justify-content:center}
.segment .icon.active{background:var(--blue);border-radius:50%;box-shadow:0 0 0 4px #d6e8f5}
.segment h3{font-size:9px;font-weight:600;color:var(--navy);margin-top:10px}
.segment p{font-size:7px;color:var(--muted);line-height:1.5;margin-top:4px}

.proposals{position:absolute;left:154px;top:612px;width:892px;height:492px;background:var(--band)}
.proposals h2{text-align:center;margin-top:28px;font-size:19px;font-style:italic;font-weight:600;color:var(--blue-dark)}
.proposals .lead{text-align:center;font-size:7.5px;color:var(--muted);line-height:1.5;margin:6px auto 0;width:300px}
.gallery{position:absolute;left:0;top:113px;width:892px;height:307px;display:grid;grid-template-columns:repeat(4,1fr);grid-template-rows:repeat(2,1fr)}
.tile{position:relative}
.t1{background:linear-gradient(160deg,#8fb6dc,#b9c1c9)}
.t2{background:linear-gradient(160deg,#2c2f35,#4a5058)}
.t3{background:linear-gradient(160deg,#7fb0de,#c8d3dc)}
.t4{background:linear-gradient(160deg,#98bedf,#b6ada2)}
.t5{background:linear-gradient(160deg,#8ab2da,#aaa59c)}
.t6{background:linear-gradient(160deg,#8cb0d4,#8d847a)}
.t7{background:linear-gradient(160deg,#80b0de,#d3d9de)}
.t8{background:linear-gradient(160deg,#4f8acc,#5d7186)}
.tile-caption{position:absolute;left:0;right:0;top:60px;text-align:center;color:var(--white)}
.tile-caption strong{display:block;font-size:12px;font-style:italic;font-weight:600}
.tile-caption span{font-size:7px;opacity:.85}
.band{position:absolute;left:0;top:420px;width:892px;height:72px;background:var(--blue);display:flex;align-items:center;justify-content:center;font-size:16px;font-style:italic;color:#e3f1fb}
.band b{font-weight:700;color:var(--white)}

.features{position:absolute;left:330px;top:1150px;width:560px;display:flex;justify-content:space-between}
.feature{display:flex;gap:10px;width:170px}
.feature h4{font-size:8.5px;font-weight:600;color:var(--navy)}
.feature p{font-size:6.5px;color:var(--muted);line-height:1.5;margin-top:3px}
</style>
</head>
<body>
<div class="page">

  <div class="topbar">
    <span>Atendimento de segunda a sábado, das 8h às 20h · (11) 4000-0000 · Contato</span>
    <div class="social"><span></span><span></span><span></span><span></span></div>
  </div>

  <header class="header">
    <div class="brand"><span class="mark"></span>FIBRAVIA</div>
    <nav class="nav">
      <span>Início</span><span>A Empresa</span><span>Serviços</span><span>Planos</span><span>Suporte</span><span>Contato</span>
    </nav>
  </header>

  <section class="hero" role="img" aria-label="Foto de céu azul com nuvens, árvore sobre gramado e família sorrindo com notebook">
    <div class="hero-copy">
      <h1>Internet fibra óptica</h1>
      <h2>A solução que você precisa!</h2>
      <p>Conecte sua casa ou empresa à rede de fibra óptica mais estável da região, com velocidade real, TV e telefonia IP.</p>
      <div class="hero-actions">
        <span class="btn btn-primary">Saiba mais</span>
        <span class="btn btn-light">Contrate</span>
      </div>
    </div>
    <div class="hero-note"><b>Cobertura:</b> consulte a disponibilidade para o seu endereço agora mesmo</div>
  </section>

  <section class="segments">
    <div class="segment">
      <div class="icon"><svg width="24" height="24" viewBox="0 0 24 24"><path d="M3 12 L12 4 L21 12 H18 V20 H14 V15 H10 V20 H6 V12Z" fill="#2a8fd0"/></svg></div>
      <h3>Residências</h3>
      <p>Planos de fibra para toda a família, com Wi-Fi forte em todos os cômodos.</p>
    </div>
    <div class="segment">
      <div class="icon"><svg width="24" height="24" viewBox="0 0 24 24"><rect x="3" y="10" width="5" height="11" fill="#2a8fd0"/><rect x="9.5" y="4" width="5" height="17" fill="#2a8fd0"/><rect x="16" y="8" width="5" height="13" fill="#2a8fd0"/></svg></div>
      <h3>Condomínios</h3>
      <p>Infraestrutura dedicada para prédios, com instalação rápida e sem obras.</p>
    </div>
    <div class="segment">
      <div class="icon active"><svg width="22" height="22" viewBox="0 0 24 24"><rect x="4" y="9" width="4" height="12" fill="#fff"/><rect x="10" y="3" width="4" height="18" fill="#fff"/><rect x="16" y="7" width="4" height="14" fill="#fff"/></svg></div>
      <h3>Empresas</h3>
      <p>Links dedicados, telefonia IP e suporte prioritário para o seu negócio.</p>
    </div>
    <div class="segment">
      <div class="icon"><svg width="24" height="24" viewBox="0 0 24 24"><path d="M12 3 L21 8 H3Z" fill="#2a8fd0"/><rect x="5" y="10" width="2.5" height="8" fill="#2a8fd0"/><rect x="10.75" y="10" width="2.5" height="8" fill="#2a8fd0"/><rect x="16.5" y="10" width="2.5" height="8" fill="#2a8fd0"/><rect x="3" y="19" width="18" height="2" fill="#2a8fd0"/></svg></div>
      <h3>Governo</h3>
      <p>Conectividade segura para órgãos públicos, escolas e unidades de saúde.</p>
    </div>
  </section>

  <section class="proposals">
    <h2>As melhores propostas para você!</h2>
    <p class="lead">Internet, TV por assinatura e telefonia IP em planos pensados para cada perfil de cliente.</p>
    <div class="gallery">
      <div class="tile t1" role="img" aria-label="Foto de casa moderna com piscina"></div>
      <div class="tile t2" role="img" aria-label="Foto de edifício residencial escuro">
        <div class="tile-caption"><strong>Nome do cliente/empresa</strong><span>Residencial · Condomínio</span></div>
      </div>
      <div class="tile t3" role="img" aria-label="Foto de edifício comercial branco"></div>
      <div class="tile t4" role="img" aria-label="Foto de torres residenciais"></div>
      <div class="tile t5" role="img" aria-label="Foto de prédio histórico com colunas"></div>
      <div class="tile t6" role="img" aria-label="Foto de prédio de escritórios"></div>
      <div class="tile t7" role="img" aria-label="Foto de edifício moderno branco"></div>
      <div class="tile t8" role="img" aria-label="Foto de edifício envidraçado"></div>
    </div>
    <div class="band">Clientes satisfeitos em todo&nbsp;<b>Brasil!</b></div>
  </section>

  <section class="features">
    <div class="feature">
      <svg width="16" height="18" viewBox="0 0 16 18"><rect x="3" y="1" width="10" height="16" rx="2" fill="none" stroke="#9aa1a8" stroke-width="1.4"/><circle cx="8" cy="14" r="1" fill="#9aa1a8"/></svg>
      <div><h4>100% Responsive Ready</h4><p>Acesse a área do cliente em qualquer tela.</p></div>
    </div>
    <div class="feature">
      <svg width="18" height="18" viewBox="0 0 18 18"><rect x="2" y="9" width="3" height="7" fill="#9aa1a8"/><rect x="7.5" y="5" width="3" height="11" fill="#9aa1a8"/><rect x="13" y="2" width="3" height="14" fill="#9aa1a8"/></svg>
      <div><h4>SEO Optimized</h4><p>Encontre nossos planos com facilidade na busca.</p></div>
    </div>
    <div class="feature">
      <svg width="18" height="16" viewBox="0 0 18 16"><path d="M9 15 L2 8 A4 4 0 0 1 9 3 A4 4 0 0 1 16 8Z" fill="none" stroke="#9aa1a8" stroke-width="1.4"/></svg>
      <div><h4>Lovely Design</h4><p>Visual limpo e navegação simples para todos.</p></div>
    </div>
  </section>

</div>
</body>
</html>
```